Flyer for longday centre (Childcare Centre)

We need a marketing flyer for our long day (Childcare) centre targeting childcare enrolments for 2016.

The name of the childcare is: Wexbury Vale Early Childhood Learning Centre
Location: will be provided later
Telephone: will be provided later
Email: will be provided later

The message of the flyer should have limited places now available for 2016. Enrol now.

Target Market(s)

Parents and Families

Industry/Entity Type

Childcare

Font styles to use
Sans Serif

Requirements
Must have
• Come and see why more and more families are switching to Wexbury Vale.
• We invite parents to come along to explore our facilities and our children's programs.
• We also run a government approved and funded Kindergarten program.
Nice to have
• Opening hours: 6am to 6:30pm Monday to Friday

```html
<!DOCTYPE html>
<html lang="en">
<head>
<meta charset="utf-8">
<title>Wexbury Vale Early Childhood Learning Centre – Enrolments 2016</title>
<link rel="stylesheet" href="https://fonts.googleapis.com/css2?family=Arvo:wght@700&family=Roboto+Condensed:wght@400;700&family=Open+Sans:wght@400;600;700&display=swap">
<style>
  :root {
    --blue: #1d5fae;
    --blue-deep: #154c92;
    --blue-light: #5b9bd8;
    --green: #3fae49;
    --green-bright: #5cc25a;
    --purple: #5b3f91;
    --white: #ffffff;
    --ink: #2b2b2b;
    --photo-warm: #e7d6c4;
    --photo-soft: #d7e3ea;
  }
  * { margin: 0; padding: 0; box-sizing: border-box; }
  html, body { width: 849px; height: 1200px; overflow: hidden; background: var(--white); }
  .flyer {
    position: relative;
    width: 849px; height: 1200px;
    overflow: hidden;
    background: var(--white);
    font-family: "Open Sans", sans-serif;
    color: var(--ink);
  }
  .hero-photo {
    position: absolute; left: 0; top: 0;
    width: 849px; height: 460px;
    background: linear-gradient(135deg, #f4ece4 0%, var(--photo-warm) 45%, #c9d9e4 100%);
  }
  .brand {
    position: absolute; left: 16px; top: 14px;
    display: flex; align-items: center; gap: 8px;
    padding: 6px 10px;
    background: rgba(255,255,255,0.85);
  }
  .brand-dot { width: 22px; height: 22px; border-radius: 50%; background: var(--green); }
  .brand-name {
    font-family: "Roboto Condensed", sans-serif;
    font-weight: 700; font-size: 15px; line-height: 1.1;
    color: var(--blue-deep); text-transform: uppercase;
  }
  .banner {
    position: absolute; left: 0; top: 380px;
    width: 849px; height: 420px;
  }
  .headline {
    position: absolute; left: 0; top: 456px; width: 849px;
    text-align: center; color: var(--white);
    font-family: "Arvo", serif; font-weight: 700;
  }
  .headline span { display: block; }
  .headline .lead { font-size: 46px; line-height: 64px; }
  .headline .lead em { font-style: normal; font-size: 60px; }
  .headline .line { font-size: 37px; line-height: 56px; }
  .headline .name { display: inline; color: var(--green-bright); }
  .points {
    position: absolute; left: 56px; top: 672px;
    list-style: none; color: var(--white);
    font-size: 17px; font-weight: 600;
  }
  .points li { display: flex; align-items: center; gap: 10px; height: 26px; margin-bottom: 10px; }
  .points svg { flex: none; }
  .offer {
    position: absolute; left: 0; top: 748px; width: 849px;
    text-align: center; color: var(--green-bright);
    font-size: 20px; font-weight: 700; line-height: 30px;
  }
  .offer strong { color: var(--white); }
  .photo-strip {
    position: absolute; left: 0; top: 800px;
    width: 849px; height: 134px;
    display: flex; gap: 4px;
  }
  .photo-strip div { flex: 1; }
  .photo-strip div:nth-child(odd) { background: linear-gradient(160deg, #eadfd2, #cdb9a6); }
  .photo-strip div:nth-child(even) { background: linear-gradient(160deg, var(--photo-soft), #b8cbd8); }
  .contact {
    position: absolute; left: 0; top: 966px; width: 849px;
    text-align: center;
  }
  .contact .title {
    font-family: "Roboto Condensed", sans-serif; font-weight: 700;
    font-size: 54px; color: var(--green); line-height: 56px;
  }
  .contact .subtitle {
    font-family: "Roboto Condensed", sans-serif; font-weight: 400;
    font-size: 25px; color: var(--green); letter-spacing: 1px; line-height: 30px;
  }
  .contact .address { font-size: 19px; line-height: 28px; margin-top: 10px; }
  .contact .lines { font-size: 19px; line-height: 28px; }
  .contact .sep { margin: 0 18px; }
  .hours {
    position: absolute; left: 184px; top: 1146px;
    width: 481px; height: 32px; border-radius: 16px;
    background: var(--purple); color: var(--white);
    font-size: 15px; font-weight: 600; font-style: italic;
    display: flex; align-items: center; justify-content: center;
  }
</style>
</head>
<body>
<main class="flyer">
  <div class="hero-photo" role="img" aria-label="Photo of a toddler playing with colourful building blocks at a table"></div>

  <div class="brand">
    <span class="brand-dot"></span>
    <span class="brand-name">Wexbury Vale<br>Early Childhood Learning Centre</span>
  </div>

  <svg class="banner" viewBox="0 0 849 420" aria-hidden="true">
    <path d="M0 30 Q120 10 212 40 Q330 80 424 48 Q560 0 849 40 V420 H0 Z" fill="var(--blue-light)"/>
    <path d="M0 44 Q120 24 212 54 Q330 94 424 62 Q560 14 849 54 V420 H0 Z" fill="var(--blue)"/>
  </svg>

  <h1 class="headline">
    <span class="lead">Come and see <em>why</em></span>
    <span class="line">more and more families are</span>
    <span class="line">switching to <span class="name">Wexbury Vale</span></span>
  </h1>

  <ul class="points">
    <li>
      <svg width="26" height="20" viewBox="0 0 26 20"><rect width="26" height="20" rx="8" fill="var(--green)"/><path d="M7 10 l4 4 l8 -8" stroke="var(--white)" stroke-width="2.5" fill="none"/></svg>
      We invite parents to come along to explore our facilities and our children's programs.
    </li>
    <li>
      <svg width="26" height="20" viewBox="0 0 26 20"><rect width="26" height="20" rx="8" fill="var(--green)"/><path d="M7 10 l4 4 l8 -8" stroke="var(--white)" stroke-width="2.5" fill="none"/></svg>
      We also run a government approved and funded Kindergarten program.
    </li>
  </ul>

  <p class="offer">Limited places now available for 2016 – <strong>Enrol now!</strong></p>

  <div class="photo-strip">
    <div role="img" aria-label="Photo of children drawing at a table"></div>
    <div role="img" aria-label="Photo of a child reading"></div>
    <div role="img" aria-label="Photo of an educator with children"></div>
    <div role="img" aria-label="Photo of children painting"></div>
    <div role="img" aria-label="Photo of children playing together"></div>
  </div>

  <section class="contact">
    <p class="title">WEXBURY VALE</p>
    <p class="subtitle">EARLY CHILDHOOD LEARNING CENTRE</p>
    <p class="address"># 0000 Adress Line 01, Line 02, City.</p>
    <p class="lines">Telephone: 555 55555<span class="sep">|</span>Email: will be provided later</p>
  </section>

  <p class="hours">Opening : 6 am to 6:30 pm Monday to Friday</p>
</main>
</body>
</html>
```